Name of company is Bluebird Meadow Shear Sharpening and Sales.Card design basic idea; I'm thinking back side just showing a sharp BLUEBIRD MEADOW. Front side: I'm thinking a tiger showing teeth and claws.With the words "Bluebird Meadow" larger type emphasized on one line.Then "Shear Sharpening and Sales" on the next line.Other info on front of card should be my name and phone #'s and address: Marcus Pellingham P (407)555-0174 CP (321)555-0138 My address is NOT to be emphasized.Can go at bottom of card. It is: 5127 Brennigan Lane Orlando FL 32899 If all that's too much to fit without looking cluttered than maybe the claw on the front with all the contact info. and just the Tiger on back of card. Whichever looks best.

Target Market(s)

Beauty Salons

Industry/Entity Type

It Company

Contact Information for Business Card

The 2 images,the claw and the tiger,could be either illustrations or photos.Whatever looks best.Got to be eye grabbing either way.

Requirements
Must have
• Contact info. Must be in color. And emphasize the identity. BLUEBIRD MEADOW.Tiger on one side.Showing TEETH. Bluebird Meadow on the other side. Showing the CLAW. .Both pics must emphasize SHARPNESS...This is a shear SHARPENING business. If one of the claw pics shows cutting grooves into something that's fine too. Card must show sharpness of the claw blade somehow.
Nice to have
• Attention grabbing. Images should jump off the card!
Should not have
• No boring cuddly tiger pics showing no teeth or claws or dull teeth or claws. No Black and whites.. No extra words other than what I've listed.

```html
<!DOCTYPE html>
<html lang="en">
<head>
<meta charset="utf-8">
<title>Bluebird Meadow Shear Sharpening and Sales – Business Card</title>
<link href="https://fonts.googleapis.com/css2?family=Roboto+Condensed:wght@400&display=swap" rel="stylesheet">
<style>
  :root {
    --backdrop: #e1e8eb;
    --card: #f7f9fb;
    --brand-deep: #1787bb;
    --brand-mid: #1a9fd3;
    --brand-bright: #14b8e3;
    --rule-grey: #6f7479;
    --faint-blue: #c9d8e8;
  }
  * { margin: 0; padding: 0; box-sizing: border-box; }
  html, body {
    width: 1200px; height: 1200px; overflow: hidden;
    background: var(--backdrop);
    font-family: "Roboto Condensed", "Arial Narrow", sans-serif;
  }
  .canvas { position: relative; width: 1200px; height: 1200px; }
  .card {
    position: absolute; left: 251px; width: 708px; height: 404px;
    background: var(--card); overflow: hidden;
  }
  .card--front { top: 137px; }
  .card--back { top: 637px; }

  .card__band { position: absolute; left: 0; width: 708px; height: 24px; }
  .card--front .card__band { bottom: 0; }
  .card--back .card__band { top: 0; }

  .front__illustration {
    position: absolute; left: 161px; top: 73px; width: 394px; height: 206px;
    border-radius: 40px;
    background: radial-gradient(ellipse at center, #5aa9d3 0%, #a9d1e8 55%, rgba(247,249,251,0) 80%);
  }
  .front__name {
    position: absolute; left: 0; width: 708px; top: 272px;
    text-align: center; color: var(--brand-deep);
    font-size: 46px; line-height: 1; letter-spacing: 0.5px;
  }
  .front__rule {
    position: absolute; left: 222px; top: 324px; width: 254px; height: 2px;
    background: var(--rule-grey);
  }
  .front__tagline {
    position: absolute; left: 0; width: 708px; top: 331px;
    text-align: center; color: var(--brand-deep);
    font-size: 24px; line-height: 1.2;
  }

  .back__illustration {
    position: absolute; right: 0; top: 24px; width: 220px; height: 380px;
    background: linear-gradient(200deg, var(--faint-blue) 0%, rgba(201,216,232,0.6) 50%, rgba(247,249,251,0) 100%);
  }
  .back__person {
    position: absolute; left: 43px; top: 186px;
    color: var(--brand-deep); font-size: 37px; line-height: 1;
  }
  .back__contact {
    position: absolute; left: 43px; top: 315px;
    color: var(--brand-deep); font-size: 16px; line-height: 21px;
  }
</style>
</head>
<body>
<div class="canvas">

  <section class="card card--front">
    <div class="front__illustration" role="img" aria-label="Illustration of a roaring tiger with bared teeth and sharp claws tearing through"></div>
    <h1 class="front__name">BLUEBIRD MEADOW</h1>
    <div class="front__rule"></div>
    <p class="front__tagline">Shear Sharpening and Sales</p>
    <svg class="card__band" viewBox="0 0 708 24" aria-hidden="true">
      <polygon points="0,0 321,0 337,24 0,24" fill="var(--brand-deep)"/>
      <polygon points="339,0 366,0 382,24 355,24" fill="var(--brand-mid)"/>
      <polygon points="383,0 433,0 450,24 398,24" fill="var(--brand-bright)"/>
    </svg>
  </section>

  <section class="card card--back">
    <svg class="card__band" viewBox="0 0 708 24" aria-hidden="true">
      <polygon points="258,0 307,0 323,24 276,24" fill="var(--brand-bright)"/>
      <polygon points="325,0 354,0 370,24 339,24" fill="var(--brand-mid)"/>
      <polygon points="370,0 708,0 708,24 389,24" fill="var(--brand-deep)"/>
    </svg>
    <div class="back__illustration" role="img" aria-label="Faint illustration of a snarling tiger head with claw slashes"></div>
    <h2 class="back__person">Marcus Pellingham</h2>
    <p class="back__contact">P (407)555-0174, CP (321)555-0138<br>5127 Brennigan Lane Orlando FL 32899</p>
  </section>

</div>
</body>
</html>
```